Premium stylish simple clever card design for high end construction company.

I need a business card designed that is a standard size and shape (square edges) that is black in colour, with black edges. All text is to be either grey/silver or yellow/gold. On the front I want the logo (supplied as attachment g5) to be embossed or raised to give a texture. I also want the name of my company "The Kestrel Vault (larger font) construction co. (smaller font)" I like the clean style (found in attachment 56419286) of the black background with silver text. But the triangle is to be gold/yellow.

On the back needs to have my contact details. In silver or gold text.

Liam Porter - Builder
Liam@thekestrelvault.com.au
www.thekestrelvault.com.au
0427391065
Lic 517904k
PO BOX 739 Narrabeen NSW 2101

Must look simple, elegant and precise.

My work is of the utmost quality and my business card needs to project that. It needs to be simple and precise. It should scream luxury and confidence. Feel free to get creative with the font and font size. If you google "The Kestrel Vault" you will see it has links to great architecture, art, nature and the fibonacci sequence so i am open to using these ideas also.

Target Market(s)

High End home owners. 30-70 year olds.

Industry/Entity Type

Residential Construction

Contact Information for Business Card

Logo and company name on front. Contact details on back.

Font styles to use
Serif
Sans Serif

Colors
ffcf3e

Requirements
Must have
• black background
Nice to have
• debossed logo (silver and gold)
• debased company name (silver)
Should not have
• It should not look like a standard construction business card with pictures of hammers or tools etc.

```html
<!DOCTYPE html>
<html lang="en">
<head>
<meta charset="utf-8">
<title>The Kestrel Vault – Business Card</title>
<link rel="stylesheet" href="https://fonts.googleapis.com/css2?family=Questrial&family=Open+Sans:wght@600;700&family=Arimo:wght@400;700&display=swap">
<style>
  :root {
    --bg: #000000;
    --silver: #e4e4e4;
    --silver-mid: #c9c9c9;
    --gold: #f7cf3c;
    --gold-rule: #c99d2a;
    --white: #ffffff;
  }
  * { margin: 0; padding: 0; box-sizing: border-box; }
  html, body {
    width: 1016px;
    height: 1200px;
    overflow: hidden;
    background: var(--bg);
  }
  .sheet {
    position: relative;
    width: 1016px;
    height: 1200px;
    background: var(--bg);
  }
  .card-face {
    position: absolute;
    left: 0;
    width: 1016px;
    height: 600px;
  }
  .card-front { top: 0; }
  .card-back { top: 606px; height: 594px; }
  .face-divider {
    position: absolute;
    left: 0;
    top: 598px;
    width: 1016px;
    height: 6px;
    background: var(--gold-rule);
  }
  .brand-dot {
    position: absolute;
    left: 50%;
    transform: translateX(-50%);
    border-radius: 50%;
    background: var(--silver-mid);
  }
  .card-front .brand-dot { top: 196px; width: 84px; height: 84px; }
  .card-back .brand-dot { top: 64px; width: 44px; height: 44px; }
  .brand-name {
    position: absolute;
    left: 0;
    width: 100%;
    text-align: center;
    font-family: "Questrial", sans-serif;
    color: var(--silver);
    text-transform: uppercase;
    white-space: nowrap;
  }
  .card-front .brand-name { top: 340px; font-size: 62px; letter-spacing: 1px; }
  .card-back .brand-name { top: 142px; font-size: 32px; letter-spacing: 0.5px; }
  .holder-name {
    position: absolute;
    top: 296px;
    left: 0;
    width: 100%;
    text-align: center;
    font-family: "Open Sans", sans-serif;
    font-weight: 700;
    font-size: 60px;
    letter-spacing: 3px;
    color: var(--gold);
    line-height: 1;
  }
  .holder-role {
    position: absolute;
    top: 360px;
    left: 0;
    width: 100%;
    text-align: center;
    font-family: "Open Sans", sans-serif;
    font-weight: 600;
    font-size: 27px;
    letter-spacing: 1.5px;
    color: var(--white);
    line-height: 1;
  }
  .contact-line {
    position: absolute;
    top: 514px;
    left: 0;
    width: 100%;
    text-align: center;
    font-family: "Arimo", sans-serif;
    font-size: 29px;
    color: var(--white);
    white-space: nowrap;
    line-height: 1;
  }
  .contact-line .sep { margin: 0 12px; }
  .contact-line .licence { font-weight: 700; }
</style>
</head>
<body>
  <main class="sheet">
    <section class="card-face card-front">
      <span class="brand-dot"></span>
      <h1 class="brand-name">The Kestrel Vault</h1>
    </section>

    <div class="face-divider"></div>

    <section class="card-face card-back">
      <span class="brand-dot"></span>
      <p class="brand-name">The Kestrel Vault</p>
      <h2 class="holder-name">LIAM PORTER</h2>
      <p class="holder-role">BUILDER</p>
      <p class="contact-line">
        <span class="email">Liam@thekestrelvault.com.au</span><span class="sep">|</span><span class="phone">0427391065</span><span class="sep">|</span><span class="licence">Lic 517904k</span>
      </p>
    </section>
  </main>
</body>
</html>
```